New emergency medical service needs a marketing flyer for prospective customers

We need a tri fold brochure on an 8.5 X 11 stock for a new emergency medical service in Pennsylvania. We provide basic first aid and now Covid-19 pre screening and temperature monitoring for special events, large gatherings and businesses. Examples of these would be but not limited to: Sporting events, carnivals, festivals, craft shows, warehouses, churches, manufacturing facilities, industrial buildings, large construction sites, multi occupancy officer buildings. The market for this is pretty much untouched and endless. we would like to use gray as the back ground color and obviously our logo. The final design should grab their attention and communicate the importance of having trained and certified professionals at their event or facility. We want to give them that piece of mind they are in good hands with us.

Target Market(s)

primary focus is going to be on businesses with large offices, large buildings or lots of foot traffic in and out of the building

Requirements
Must have
• gray background, pictures, company phone # , company web site, and contact email address. I will provide all that information to the winner to add at the end.
Nice to have
• pictures that covers the whole front cover with logo at top

```html
<!DOCTYPE html>
<html lang="en">
<head>
<meta charset="utf-8">
<title>Ridgeline Medical – Tri-fold Brochure</title>
<link rel="stylesheet" href="https://fonts.googleapis.com/css2?family=Montserrat:wght@400;500;600;700;800&family=Oswald:wght@600&display=swap">
<style>
  :root {
    --blue: #0a0ab4;
    --blue-deep: #0606a0;
    --teal: #0bb39f;
    --gray: #6a6a6a;
    --gray-dark: #575757;
    --paper: #eceef0;
    --white: #ffffff;
    --ink: #151515;
    --stage: #f1f1f1;
  }
  * { box-sizing: border-box; margin: 0; padding: 0; }
  html, body { width: 1200px; height: 800px; overflow: hidden; }
  body {
    background: var(--stage);
    font-family: "Montserrat", Arial, sans-serif;
    position: relative;
  }
  .brochure {
    position: absolute;
    left: 105px; top: 17px;
    width: 990px; height: 766px;
    box-shadow: 0 8px 24px rgba(0,0,0,.15);
    overflow: hidden;
  }
  .brochure__art { position: absolute; inset: 0; }
  .block { position: absolute; }

  /* Left panel */
  .fields { left: 40px; top: 468px; width: 280px; color: var(--white); }
  .fields__title {
    font-size: 25px; font-weight: 400; letter-spacing: 1px;
    padding-bottom: 6px; border-bottom: 1px solid var(--white);
    width: 250px;
  }
  .fields__title strong { color: var(--teal); font-weight: 700; }
  .fields__list { list-style: none; margin-top: 10px; }
  .fields__list li {
    position: relative; padding-left: 26px;
    font-size: 14px; font-weight: 600; line-height: 18.5px; letter-spacing: .3px;
    margin-bottom: 1px;
  }
  .fields__list li::before {
    content: ""; position: absolute; left: 2px; top: 3px;
    width: 11px; height: 11px; border: 1.5px solid var(--teal); border-radius: 50%;
  }
  .fields__list li::after {
    content: ""; position: absolute; left: 6px; top: 5.5px;
    width: 3px; height: 5px; border: solid var(--teal); border-width: 0 1.5px 1.5px 0;
    transform: rotate(45deg);
  }

  /* Middle panel */
  .offer { left: 352px; top: 138px; width: 290px; font-size: 14.5px; line-height: 21px; font-weight: 500; color: var(--ink); }
  .offer b { color: var(--blue); font-weight: 700; }
  .promise {
    left: 395px; top: 340px; width: 200px; height: 190px;
    display: flex; align-items: center; justify-content: center; text-align: center;
    color: var(--white); font-weight: 800; font-size: 14.5px; line-height: 20px; letter-spacing: .5px;
  }
  .contact { left: 360px; top: 560px; width: 270px; color: var(--white); text-align: center; }
  .contact__title { font-size: 19px; font-weight: 500; letter-spacing: 1.5px; }
  .contact__rule { display: flex; align-items: center; gap: 8px; margin: 4px 0 8px; }
  .contact__rule span { flex: 1; height: 1px; background: var(--teal); }
  .contact__line { font-size: 12.5px; font-weight: 500; line-height: 19px; display: flex; align-items: center; justify-content: center; gap: 6px; }
  .icon { width: 12px; height: 12px; flex: none; }

  /* Right panel */
  .brand { left: 690px; top: 32px; width: 270px; display: flex; align-items: center; gap: 10px; }
  .brand__dot { width: 30px; height: 30px; border-radius: 50%; background: var(--blue); flex: none; }
  .brand__name { font-size: 24px; font-weight: 800; color: var(--blue); letter-spacing: .3px; }
  .cover-title { left: 690px; top: 548px; width: 280px; color: var(--white); }
  .cover-title__lead { font-size: 36px; font-weight: 800; letter-spacing: 1px; line-height: 40px; }
  .cover-title__band {
    display: inline-block; background: var(--teal); margin: 4px 0 4px 8px;
    font-family: "Oswald", Impact, sans-serif; font-weight: 600; font-size: 27px; line-height: 34px;
    padding: 0 12px; letter-spacing: .5px;
  }
  .cover-title__place { font-size: 26px; font-weight: 800; line-height: 32px; }
  .cover-title__web {
    margin-top: 12px; display: inline-flex; align-items: center; gap: 8px;
    border: 1px solid var(--white); border-radius: 12px; padding: 2px 12px 2px 2px;
    font-size: 11px; font-weight: 500; letter-spacing: .3px;
  }
  .cover-title__globe { width: 26px; height: 18px; background: var(--teal); border-radius: 9px; display: flex; align-items: center; justify-content: center; }
</style>
</head>
<body>
<main class="brochure">
  <svg class="brochure__art" viewBox="0 0 990 766" width="990" height="766" aria-hidden="false">
    <defs>
      <linearGradient id="siteGrad" x1="0" y1="0" x2="1" y2="1">
        <stop offset="0" stop-color="#8a3d36"/>
        <stop offset=".55" stop-color="#a0523f"/>
        <stop offset="1" stop-color="#d8c24a"/>
      </linearGradient>
      <linearGradient id="wardGrad" x1="0" y1="0" x2="0" y2="1">
        <stop offset="0" stop-color="#e9ecef"/>
        <stop offset=".5" stop-color="#c9cdd2"/>
        <stop offset="1" stop-color="#b8334a"/>
      </linearGradient>
      <linearGradient id="paperGrad" x1="0" y1="0" x2="1" y2="1">
        <stop offset="0" stop-color="#f4f5f6"/>
        <stop offset="1" stop-color="#dcdfe2"/>
      </linearGradient>
    </defs>

    <!-- Left panel -->
    <rect x="0" y="0" width="330" height="766" fill="var(--gray)"/>
    <rect class="photo" x="0" y="0" width="330" height="430" fill="url(#siteGrad)" role="img" aria-label="Photo: site worker in hard hat taking the temperature of a masked colleague"/>
    <path d="M0 380 Q165 430 330 375 L330 440 L0 440 Z" fill="var(--teal)"/>
    <path d="M0 415 Q170 460 330 405 L330 766 L0 766 Z" fill="var(--blue)"/>

    <!-- Middle panel -->
    <rect x="330" y="0" width="330" height="766" fill="url(#paperGrad)" role="img" aria-label="Soft background photo of a clinical corridor"/>
    <path d="M330 0 L660 0 L660 60 Q495 150 330 80 Z" fill="var(--gray)"/>
    <path d="M330 80 Q495 150 660 60 L660 85 Q495 175 330 100 Z" fill="var(--teal)"/>
    <path d="M330 470 Q495 555 660 460 L660 766 L330 766 Z" fill="var(--blue)"/>
    <circle cx="495" cy="435" r="104" fill="var(--teal)"/>
    <circle cx="495" cy="438" r="94" fill="var(--gray)"/>

    <!-- Right panel -->
    <rect x="660" y="0" width="330" height="766" fill="var(--gray)"/>
    <rect class="photo" x="660" y="90" width="330" height="380" fill="url(#wardGrad)" role="img" aria-label="Photo: paramedics and a doctor wheeling a patient on a hospital bed"/>
    <path d="M660 0 L990 0 L990 90 L825 130 L660 90 Z" fill="var(--gray)"/>
    <path d="M660 90 L825 130 L990 90 L990 104 L825 146 L660 104 Z" fill="var(--teal)"/>
    <path d="M660 470 Q825 475 990 400 L990 470 L660 480 Z" fill="var(--teal)"/>
    <path d="M660 490 Q830 480 990 420 L990 766 L660 766 Z" fill="var(--blue)"/>

    <!-- Fold lines -->
    <line x1="330" y1="0" x2="330" y2="766" stroke="rgba(0,0,0,.12)"/>
    <line x1="660" y1="0" x2="660" y2="766" stroke="rgba(0,0,0,.12)"/>
  </svg>

  <!-- Left panel: fields -->
  <section class="block fields">
    <h2 class="fields__title">OUR <strong>FIELDS</strong></h2>
    <ul class="fields__list">
      <li>Sporting Events</li>
      <li>Carnivals</li>
      <li>Festivals</li>
      <li>Craft Shows</li>
      <li>Warehouses</li>
      <li>Churches</li>
      <li>Manufacturing Facilities</li>
      <li>Industrial Buildings</li>
      <li>Large Construction Sites</li>
      <li>Multi Occupancy Officer Buildings.</li>
      <li>and many more</li>
    </ul>
  </section>

  <!-- Middle panel -->
  <p class="block offer">
    <b>We Provide<br>Basic first aid</b> and now <b>Covid-19</b> pre screening and temperature monitoring for <b>Special Events,</b> large <b>Gatherings</b> and businesses.
  </p>
  <p class="block promise">WE HAVE<br>TRAINED AND<br>CERTIFIED<br>PROFESSIONALS<br>AT THEIR EVENT<br>OR FACILITY</p>

  <section class="block contact">
    <h2 class="contact__title">CONTACT INFO</h2>
    <div class="contact__rule">
      <span></span>
      <svg class="icon" viewBox="0 0 12 12"><path d="M6 1a3 3 0 0 0-3 3c0 2.2 3 6 3 6s3-3.8 3-6a3 3 0 0 0-3-3z" fill="none" stroke="var(--teal)" stroke-width="1.3"/><circle cx="6" cy="4" r="1" fill="var(--teal)"/></svg>
      <span></span>
    </div>
    <p class="contact__line">Address Line 1, Address Line 1</p>
    <p class="contact__line">Address Line 2</p>
    <p class="contact__line"><svg class="icon" viewBox="0 0 12 12"><path d="M3 1.5l1.6 2.2-1 1.2a6 6 0 0 0 2.9 2.9l1.2-1 2.2 1.6-.8 1.9C5 10.3 1.7 7 1.1 2.3z" fill="none" stroke="var(--teal)" stroke-width="1.1"/></svg>0100 555 210</p>
    <p class="contact__line"><svg class="icon" viewBox="0 0 12 12"><rect x="1" y="2.5" width="10" height="7" fill="none" stroke="var(--teal)" stroke-width="1.1"/><path d="M1 2.5l5 4 5-4" fill="none" stroke="var(--teal)" stroke-width="1.1"/></svg>info@ridgelinemed.com</p>
    <p class="contact__line"><svg class="icon" viewBox="0 0 12 12"><circle cx="6" cy="6" r="5" fill="none" stroke="var(--teal)" stroke-width="1.1"/><path d="M1 6h10M6 1c-2.5 3-2.5 7 0 10M6 1c2.5 3 2.5 7 0 10" fill="none" stroke="var(--teal)" stroke-width="1"/></svg>www.ridgelinemed.com</p>
  </section>

  <!-- Right panel: cover -->
  <div class="block brand">
    <span class="brand__dot"></span>
    <span class="brand__name">Ridgeline Medical</span>
  </div>

  <section class="block cover-title">
    <h1 class="cover-title__lead">EMERGENCY</h1>
    <p class="cover-title__band">MEDICAL SERVICE</p>
    <p class="cover-title__place">in Pennsylvania</p>
    <p class="cover-title__web">
      <span class="cover-title__globe"><svg class="icon" viewBox="0 0 12 12"><circle cx="6" cy="6" r="5" fill="none" stroke="var(--white)" stroke-width="1.1"/><path d="M1 6h10M6 1c-2.5 3-2.5 7 0 10M6 1c2.5 3 2.5 7 0 10" fill="none" stroke="var(--white)" stroke-width="1"/></svg></span>
      www.ridgelineMed.com
    </p>
  </section>
</main>
</body>
</html>
```